Business Card Design

Very plain simple card, Plain modern font. Background. Grey fading to black. Large Bright lime green text. Saying.

TWR-ZA.COM

Small other details in white text.

Irish Horse Sales . Livery . Stud . Shows

Mark Dabrowski
TWR
Birch Lodge
Carrowmede Lane
Thistlecombe
Lincolnshire
LN4 7JX

Email. Twrzap@mailvale.co.uk
Tel. 07482 936504

Industry/Entity Type

Business

Contact Information for Business Card

As below

```html
<!DOCTYPE html>
<html lang="en">
<head>
<meta charset="utf-8">
<title>TWR-ZA.COM Business Card</title>
<link rel="stylesheet" href="https://fonts.googleapis.com/css2?family=Russo+One&family=Open+Sans:wght@400;600;700&display=swap">
<style>
  :root {
    --sky-light: #d6d8da;
    --sky-mid: #c9cbcd;
    --band-green: #407a36;
    --lime: #5fae47;
    --fade-top: #b0b2b4;
    --fade-mid: #5a5c5e;
    --fade-bottom: #1c1d1e;
    --ink-white: #ffffff;
  }
  html, body {
    margin: 0;
    padding: 0;
    width: 1200px;
    height: 791px;
    overflow: hidden;
    background: #ffffff;
  }
  .card {
    position: relative;
    width: 1200px;
    height: 791px;
    overflow: hidden;
    font-family: "Open Sans", Arial, sans-serif;
    color: var(--ink-white);
  }
  .card__header {
    position: absolute;
    left: 0; top: 0;
    width: 1200px; height: 298px;
    background: radial-gradient(ellipse at 55% 45%, var(--sky-light) 0%, var(--sky-mid) 100%);
  }
  .card__headline {
    position: absolute;
    left: 0; top: 0;
    width: 1200px; height: 298px;
  }
  .card__headline text {
    font-family: "Russo One", Impact, sans-serif;
    font-size: 150px;
    fill: var(--lime);
  }
  .card__band {
    position: absolute;
    left: 0; top: 298px;
    width: 1200px; height: 124px;
    background: var(--band-green);
  }
  .card__tagline {
    position: absolute;
    left: 0; top: 0;
    width: 1200px; height: 124px;
  }
  .card__tagline text {
    font-family: "Open Sans", Arial, sans-serif;
    font-weight: 600;
    font-size: 34px;
    font-variant: small-caps;
    fill: var(--ink-white);
  }
  .card__body {
    position: absolute;
    left: 0; top: 422px;
    width: 1200px; height: 369px;
    background: linear-gradient(180deg, var(--fade-top) 0%, var(--fade-mid) 40%, var(--fade-bottom) 100%);
  }
  .contact-person {
    position: absolute;
    left: 79px;
    top: 448px;
  }
  .contact-person__name {
    margin: 0;
    font-weight: 600;
    font-size: 36px;
    line-height: 48px;
  }
  .contact-person__company {
    margin: 8px 0 0;
    font-weight: 600;
    font-size: 44px;
    line-height: 56px;
  }
  .contact-person__address {
    margin: 6px 0 0;
    font-style: normal;
    font-size: 29px;
    line-height: 42px;
  }
  .contact-lines {
    position: absolute;
    left: 668px;
    top: 453px;
    margin: 0;
    font-size: 30px;
    line-height: 46px;
  }
</style>
</head>
<body>
  <main class="card">
    <header class="card__header">
      <svg class="card__headline" viewBox="0 0 1200 298" aria-label="TWR-ZA.COM">
        <text x="92" y="254" textLength="983" lengthAdjust="spacingAndGlyphs">TWR-ZA.COM</text>
      </svg>
    </header>

    <section class="card__band">
      <svg class="card__tagline" viewBox="0 0 1200 124" aria-label="Irish Horse Sales . Livery . Stud . Shows">
        <text x="121" y="75" textLength="939" lengthAdjust="spacing">Irish Horse Sales . Livery . Stud . Shows</text>
      </svg>
    </section>

    <section class="card__body"></section>

    <div class="contact-person">
      <p class="contact-person__name">Mark Dabrowski</p>
      <p class="contact-person__company">TWR</p>
      <address class="contact-person__address">
        Birch Lodge<br>
        Carrowmede Lane,Thistlecombe<br>
        Lincolnshire,LN4 7JX
      </address>
    </div>

    <p class="contact-lines">
      Email. Twrzap@mailvale.co.uk<br>
      Tel. 07482 936504
    </p>
  </main>
</body>
</html>
```